Business Card Design Project

Hi,
This is a simple contest. The logo for the back of the card is deigned. See attached files. The front of the card must have :

Directors Name: Dorian
Mob:
e-mail:
Postal Address:
Web Page Adress:

It may also add words: "Leaders in Construction Project Management Services"

Target Market(s)

Business & Home owners alike

Industry/Entity Type

Business

Requirements
Must have
• See details above and logo attached
Should not have
• Images other than logo

```html
<!DOCTYPE html>
<html lang="en">
<head>
<meta charset="UTF-8">
<title>Ridgeline Projects Australia – Business Card</title>
<link rel="stylesheet" href="https://fonts.googleapis.com/css2?family=Roboto:wght@400;500&display=swap">
<style>
  :root {
    --stage: #000000;
    --card-white: #ffffff;
    --brand-blue: #079cda;
    --icon-blue: #1a9ad6;
    --text-teal: #2a6e8e;
    --band-teal: #3d88a6;
    --divider: #1c3550;
    --watermark: #dfe9f4;
  }
  * { margin: 0; padding: 0; box-sizing: border-box; }
  html, body {
    width: 959px; height: 1200px; overflow: hidden;
    background: var(--stage);
    font-family: "Roboto", Arial, sans-serif;
  }
  .canvas { position: relative; width: 959px; height: 1200px; }

  .card { position: absolute; left: 27px; width: 903px; height: 557px; overflow: hidden; }
  .card-front { top: 27px; background: var(--card-white); }
  .card-back { top: 614px; background: var(--brand-blue); }

  .holder { position: absolute; top: 40px; left: 0; width: 100%; text-align: center; }
  .holder-name { font-size: 44px; font-weight: 400; color: var(--text-teal); line-height: 1.1; }
  .holder-title {
    font-size: 25px; font-weight: 400; color: var(--icon-blue);
    letter-spacing: 22px; margin-left: 22px; line-height: 1.1;
  }

  .contact-tint {
    position: absolute; left: 329px; top: 219px; width: 199px; height: 204px;
    background: var(--watermark);
  }
  .divider {
    position: absolute; left: 428px; top: 180px; width: 3px; height: 273px;
    background: var(--divider);
  }

  .contact-icon {
    position: absolute; width: 52px; height: 52px; background: var(--icon-blue);
  }
  .contact-icon svg { width: 100%; height: 100%; display: block; }
  .icon-phone  { left: 344px; top: 233px; }
  .icon-email  { left: 344px; top: 348px; }
  .icon-postal { left: 465px; top: 233px; }
  .icon-web    { left: 465px; top: 348px; }

  .contact-text {
    position: absolute; font-size: 25px; color: var(--text-teal); line-height: 52px; white-space: nowrap;
  }
  .contact-left { right: 579px; text-align: right; }
  .contact-right { left: 538px; }
  .row-top { top: 233px; }
  .row-bottom { top: 348px; }

  .tagline-band {
    position: absolute; left: 0; bottom: 0; width: 100%; height: 48px;
    background: var(--band-teal);
    color: var(--card-white); text-align: center;
    font-size: 24px; font-weight: 500; letter-spacing: 1.6px; line-height: 48px;
  }

  .company-name {
    position: absolute; left: 0; top: 0; width: 100%; height: 100%;
    display: flex; align-items: center; justify-content: center;
    color: var(--card-white); font-size: 46px; font-weight: 500;
  }
</style>
</head>
<body>
<div class="canvas">

  <section class="card card-front">
    <div class="holder">
      <div class="holder-name">Dorian Lastname</div>
      <div class="holder-title">DIRECTOR</div>
    </div>

    <div class="contact-tint"></div>
    <div class="divider"></div>

    <div class="contact-icon icon-phone">
      <svg viewBox="0 0 52 52" aria-hidden="true">
        <rect x="17" y="9" width="18" height="34" rx="3" fill="none" stroke="#fff" stroke-width="2.5"/>
        <rect x="20" y="14" width="12" height="20" fill="#fff"/>
        <circle cx="26" cy="38.5" r="1.8" fill="#fff"/>
      </svg>
    </div>
    <div class="contact-icon icon-email">
      <svg viewBox="0 0 52 52" aria-hidden="true">
        <path d="M9 22 L26 10 L43 22 V42 H9 Z" fill="none" stroke="#fff" stroke-width="2.5" stroke-linejoin="round"/>
        <path d="M9 22 L26 34 L43 22" fill="none" stroke="#fff" stroke-width="2.5"/>
        <text x="26" y="28" text-anchor="middle" font-family="Roboto, Arial, sans-serif" font-size="14" font-weight="500" fill="#fff">@</text>
      </svg>
    </div>
    <div class="contact-icon icon-postal">
      <svg viewBox="0 0 52 52" aria-hidden="true">
        <rect x="9" y="13" width="34" height="26" fill="none" stroke="#fff" stroke-width="2.5"/>
        <rect x="31" y="17" width="8" height="8" fill="#fff"/>
        <line x1="14" y1="25" x2="27" y2="25" stroke="#fff" stroke-width="2"/>
        <line x1="14" y1="30" x2="38" y2="30" stroke="#fff" stroke-width="2"/>
        <line x1="14" y1="35" x2="38" y2="35" stroke="#fff" stroke-width="2"/>
      </svg>
    </div>
    <div class="contact-icon icon-web">
      <svg viewBox="0 0 52 52" aria-hidden="true">
        <g fill="none" stroke="#fff" stroke-width="2.2">
          <circle cx="26" cy="26" r="15"/>
          <ellipse cx="26" cy="26" rx="7" ry="15"/>
          <line x1="11" y1="26" x2="41" y2="26"/>
          <line x1="26" y1="11" x2="26" y2="41"/>
          <path d="M14 18 H38 M14 34 H38"/>
        </g>
      </svg>
    </div>

    <div class="contact-text contact-left row-top">0000-000-0000</div>
    <div class="contact-text contact-left row-bottom">emailhere@rpa.com</div>
    <div class="contact-text contact-right row-top">Postal Adress Here</div>
    <div class="contact-text contact-right row-bottom">www.webpagehere.com</div>

    <div class="tagline-band">"Leaders in Construction Project Management Services"</div>
  </section>

  <section class="card card-back">
    <div class="company-name">Ridgeline Projects Australia</div>
  </section>

</div>
</body>
</html>
```